Harbor: Social Media Image: FLU

We are looking to create a social media graphic that can be used. We would like it to mimic this --> https://www.plvo.org/This-is-your-shot_01.png
Will contain the:
-- Campaign Name: HARBOR,
-- Moto: Protect Your Community. Protect Your Elders. Stay Vaccinated.
-- QT7 logo
-- Language: Learn more about getting vaccinated against COVID-19
-- Picture of real person

Please reference our QT7 homepage for visual inspiration qtbridged.org or look here: https://qtbridged.org/resources/dementia-risk-reduction-flyers-healthy-heart-healthy-brain/

```html
<!DOCTYPE html>
<html lang="en">
<head>
<meta charset="utf-8">
<title>Harbor – Stay Vaccinated</title>
<link rel="stylesheet" href="https://fonts.googleapis.com/css2?family=Bebas+Neue&family=Montserrat:wght@700&display=swap">
<style>
  :root {
    --teal: #2a9ea8;
    --clay: #a55550;
    --clay-dark: #8c4440;
    --pattern: #c9b8b5;
    --white: #ffffff;
    --yellow: #f5e51b;
    --logo-teal: #2a8f95;
    --logo-red: #c0343c;
  }
  * { margin: 0; padding: 0; box-sizing: border-box; }
  html, body { width: 1200px; height: 1200px; overflow: hidden; background: var(--teal); }
  .poster { position: relative; width: 1200px; height: 1200px; background: var(--teal); }

  .pattern-band { position: absolute; background: var(--pattern); }
  .pattern-top { left: 17px; top: 17px; width: 1166px; height: 46px; }
  .pattern-bottom { left: 17px; top: 1137px; width: 1166px; height: 46px; }
  .pattern-left { left: 17px; top: 63px; width: 46px; height: 1074px; }
  .pattern-right { left: 1137px; top: 63px; width: 46px; height: 1074px; }

  .field {
    position: absolute; left: 63px; top: 63px; width: 1074px; height: 1074px;
    border: 3px solid var(--white);
    background: radial-gradient(ellipse at 30% 20%, #b26059 0%, var(--clay) 45%, var(--clay-dark) 100%);
    overflow: hidden;
  }
  .elders-photo {
    position: absolute; left: 322px; top: 110px; width: 815px; height: 1030px;
    background:
      linear-gradient(90deg, rgba(165,85,80,0) 0%, rgba(165,85,80,0) 100%),
      radial-gradient(ellipse at 78% 40%, #9a2f9a 0%, #7d2a7a 30%, rgba(125,42,122,0) 55%),
      radial-gradient(ellipse at 45% 80%, #c2402a 0%, #3a2a45 35%, rgba(58,42,69,0) 60%),
      radial-gradient(ellipse at 88% 85%, #f08a3a 0%, rgba(240,138,58,0) 40%);
  }

  .headline-box {
    position: absolute; left: 120px; top: 120px; width: 610px; height: 182px;
    border: 3px solid var(--white); border-bottom: none;
  }
  .headline {
    position: absolute; left: 150px; top: 125px;
    font-family: "Bebas Neue", sans-serif; font-size: 190px; line-height: 1;
    color: var(--white); letter-spacing: 2px;
  }
  .headline-arrow { position: absolute; left: 118px; top: 296px; }

  .motto { position: absolute; left: 120px; top: 375px; text-shadow: 0 2px 6px rgba(0,0,0,.35); }
  .motto-lead {
    display: block; font-family: "Montserrat", sans-serif; font-weight: 700;
    font-size: 40px; line-height: 1; color: var(--yellow); letter-spacing: 1px;
  }
  .motto-key {
    display: block; font-family: "Bebas Neue", sans-serif; font-size: 112px;
    line-height: .9; color: var(--white); margin-bottom: 14px;
  }

  .logo-card {
    position: absolute; left: 122px; top: 884px; width: 384px; height: 88px;
    background: var(--white); display: flex; align-items: center; gap: 14px; padding: 0 16px;
  }
  .logo-mark { width: 14px; height: 14px; background: var(--logo-teal); }
  .logo-name {
    font-family: "Montserrat", sans-serif; font-weight: 700; font-size: 20px;
    line-height: 1.15; color: var(--logo-red);
  }

  .drop-arrows { position: absolute; left: 1066px; top: 830px; }

  .cta-band {
    position: absolute; left: 17px; top: 1028px; width: 1166px; height: 69px;
    background: var(--teal); display: flex; align-items: center; justify-content: center;
    font-family: "Montserrat", sans-serif; font-weight: 700; font-size: 27px;
    color: var(--white); letter-spacing: .5px;
  }
</style>
</head>
<body>
<main class="poster">
  <div class="pattern-band pattern-top" role="img" aria-label="Zigzag woven border pattern"></div>
  <div class="pattern-band pattern-bottom" role="img" aria-label="Zigzag woven border pattern"></div>
  <div class="pattern-band pattern-left" role="img" aria-label="Zigzag woven border pattern"></div>
  <div class="pattern-band pattern-right" role="img" aria-label="Zigzag woven border pattern"></div>

  <div class="field"></div>
  <div class="elders-photo" role="img" aria-label="Photo of two Native elder women in traditional dress with turquoise jewelry, one seated wrapped in a patterned blanket"></div>

  <div class="headline-box"></div>
  <h1 class="headline">HARBOR</h1>
  <svg class="headline-arrow" width="660" height="40" viewBox="0 0 660 40">
    <line x1="0" y1="6" x2="59" y2="6" stroke="#fff" stroke-width="3"/>
    <g fill="#f5e51b">
      <polygon points="59,-8 86,6 59,20" transform="translate(0,6)"/>
      <polygon points="88,-8 115,6 88,20" transform="translate(0,6)"/>
      <polygon points="117,-8 144,6 117,20" transform="translate(0,6)"/>
      <polygon points="146,-8 173,6 146,20" transform="translate(0,6)"/>
    </g>
    <line x1="180" y1="12" x2="630" y2="12" stroke="#fff" stroke-width="3"/>
    <polygon points="625,-2 655,12 625,26" fill="#fff"/>
  </svg>

  <div class="motto">
    <span class="motto-lead">PROTECT YOUR</span>
    <span class="motto-key">COMMUNITY.</span>
    <span class="motto-lead">PROTECT YOUR</span>
    <span class="motto-key">ELDERS.</span>
    <span class="motto-lead">STAY</span>
    <span class="motto-key">VACCINATED.</span>
  </div>

  <div class="logo-card">
    <span class="logo-mark"></span>
    <span class="logo-name">QT7 · Quillwater Tribal<br>Elders Alliance</span>
  </div>

  <svg class="drop-arrows" width="60" height="204" viewBox="0 0 60 204">
    <g fill="#fff">
      <polygon points="0,0 60,0 30,46"/>
      <polygon points="0,52 60,52 30,98"/>
      <polygon points="0,104 60,104 30,150"/>
      <polygon points="0,156 60,156 30,202"/>
    </g>
  </svg>

  <div class="cta-band">LEARN MORE ABOUT GETTING VACCINATED AGAINST COVID-19</div>
</main>
</body>
</html>
```